Visitenkarten-Design
Zielgruppe
Elektro und Automatisierungstechnik
Zielgruppe: Industriekunden
Aufgabenstellung
Zweiseitig farbig
Querformat 8,5*5,5cm
modernes, innovatives und zuverlässiges Unternehmen
Vorhandenes Logo muss integriert werden. Siehe Anhang

```html
<!DOCTYPE html>
<html lang="de">
<head>
<meta charset="utf-8">
<title>Visitenkarte – Brettlinger Elektrotechnik</title>
<link rel="stylesheet" href="https://fonts.googleapis.com/css2?family=Montserrat:wght@400;600;700&display=swap">
<style>
  :root {
    --backdrop: #e2e2e2;
    --navy: #183758;
    --paper: #ffffff;
  }
  * { margin: 0; padding: 0; box-sizing: border-box; }
  html, body {
    width: 1200px; height: 1200px; overflow: hidden;
    background: var(--backdrop);
    font-family: "Montserrat", sans-serif;
  }
  .card {
    position: absolute;
    left: 322px;
    width: 555px;
    height: 359px;
  }
  .card--front { top: 180px; background: var(--paper); }
  .card--back  { top: 600px; background: var(--navy); color: var(--paper); }

  .wordmark {
    position: absolute;
    left: 0; right: 0; top: 110px;
    display: flex;
    justify-content: center;
    align-items: center;
    gap: 16px;
    color: var(--navy);
    font-weight: 600;
  }
  .wordmark__square {
    width: 22px; height: 22px;
    background: var(--navy);
  }
  .wordmark__text { line-height: 1.05; }
  .wordmark__name { display: block; font-size: 40px; letter-spacing: 0.5px; }
  .wordmark__trade { display: block; font-size: 22px; letter-spacing: 3px; margin-top: 4px; }

  .person {
    position: absolute;
    left: 54px; top: 86px;
  }
  .person__name { font-size: 20px; font-weight: 700; letter-spacing: 0.2px; }
  .person__role { font-size: 13.5px; font-weight: 400; margin-top: 6px; letter-spacing: 0.3px; }

  .divider {
    position: absolute;
    left: 54px; right: 0; top: 157px;
    height: 1.5px;
    background: var(--paper);
  }

  .contact {
    position: absolute;
    top: 252px;
    font-size: 12.5px;
    line-height: 18px;
    letter-spacing: 0.2px;
    font-style: normal;
    white-space: nowrap;
  }
  .contact--address { left: 54px; }
  .contact--reach { left: 292px; }
  .contact__company { font-weight: 700; font-size: 11.5px; letter-spacing: 0.1px; }
</style>
</head>
<body>
  <section class="card card--front">
    <div class="wordmark">
      <span class="wordmark__square"></span>
      <span class="wordmark__text">
        <span class="wordmark__name">BRETTLINGER</span>
        <span class="wordmark__trade">ELEKTROTECHNIK</span>
      </span>
    </div>
  </section>

  <section class="card card--back">
    <div class="person">
      <p class="person__name">Jonas Peter Brettlinger</p>
      <p class="person__role">Geschäftsführer</p>
    </div>
    <div class="divider"></div>
    <address class="contact contact--address">
      <span class="contact__company">Brettlinger Elektrotechnik GmbH</span><br>
      Mühlweg 7<br>
      87654 Talbrunn
    </address>
    <address class="contact contact--reach">
      +49 98 765 43 21<br>
      kontakt@brettlinger-elektro.de<br>
      www.brettlinger-elektro.de
    </address>
  </section>
</body>
</html>
```